Corporate Design für Helga Brunnmeier
Zielgruppe
Ich bin eine Beraterin mit sehr unterschiedlichen Zugängen. Zum einen mache ich hellsichtige Beratungen, zum anderen Organisationsberatungen und Coaching. Ich habe für jedes Problem eine Lösung. Es handelt sich um eine außergewöhnliche Dienstleistung. Es geht um mehr Klarheit und Transparenz. Meine Kunden sind sowohl Privatpersonen, als auch Firmeninhaber und Firmenchefs kleiner und großer Unternehmen.
I am a consultant with different approaches. On one hand I am doing perceptive consulting, on the other hand I do systemic consulting of organizations and coaching. I find a solution for every problem. It is an outstanding service. Clearness and transparency are mainly wished. My clients are private persons as well as company owners and managers of small and huge companies.
Aufgabenstellung
Das Logo soll nur den Vor- und Nachnamen beinhalten und elegant, weiblich, warm, herzlich sein sowie Lebensfreude, Erleichterung und Exklusivität suggerieren.
Das Logo soll auf den Visitenkarten auf der Rückseite geprägt werden. Es soll aber auch für Briefpapier, Powerpoint-Vorlage und Website gut tauglich sein.
The logo should include only my full name. It should be elegant, female, warm, sincere as well as suggest joie de vivre, easement and exclusiveness.
The logo should be stamped on the back side of the business cards. It should also work for letters, PowerPoint presentations and on the website.

```html
<!DOCTYPE html>
<html lang="de">
<head>
<meta charset="utf-8">
<title>Helga Brunnmeier – Corporate Design</title>
<link href="https://fonts.googleapis.com/css2?family=Roboto+Condensed:wght@400;700&display=swap" rel="stylesheet">
<style>
  :root {
    --gold: #b59a62;
    --cream: #ecdfc6;
    --ink: #8a8a8a;
    --paper: #ffffff;
    --shadow: 0 1px 4px rgba(0,0,0,.35);
  }
  html, body {
    margin: 0; padding: 0;
    width: 1200px; height: 1155px;
    overflow: hidden;
    background: var(--paper);
    font-family: "Roboto Condensed", sans-serif;
  }
  .canvas { position: relative; width: 1200px; height: 1155px; }

  .wordmark {
    position: absolute;
    white-space: nowrap;
    font-weight: 700;
    text-transform: uppercase;
    color: var(--gold);
  }
  .wordmark--hero {
    left: 756px; top: 160px; width: 390px;
    text-align: center;
    font-size: 27px; letter-spacing: 0.42em;
  }

  /* Letterhead */
  .letterhead {
    position: absolute; left: 86px; top: 190px;
    width: 583px; height: 826px;
    background: var(--paper);
    box-shadow: var(--shadow);
    overflow: hidden;
  }
  .letterhead .wordmark {
    left: 0; width: 583px; top: 79px; text-align: center;
    font-size: 12px; letter-spacing: 0.5em;
  }
  .sender-line {
    position: absolute; left: 64px; top: 163px;
    font-size: 7.5px; color: var(--ink);
    border-bottom: 0.6px solid var(--ink);
    padding: 0 2px 1px;
  }
  .sender-line .dot {
    display: inline-block; width: 3px; height: 3px; border-radius: 50%;
    background: var(--gold); margin: 0 7px; vertical-align: middle;
  }
  .address-block, .footer-block {
    position: absolute; font-size: 8px; line-height: 12.5px; color: var(--ink);
  }
  .address-block { left: 430px; top: 163px; }
  .address-block p, .footer-block p { margin: 0 0 10px; }
  .footer-block { left: 436px; top: 703px; }
  .wave { position: absolute; left: 0; bottom: 0; display: block; }

  /* Business cards */
  .card {
    position: absolute; width: 378px; height: 245px;
    box-shadow: var(--shadow); overflow: hidden;
  }
  .card--front { left: 733px; top: 456px; background: var(--gold); }
  .card--front .wordmark {
    left: 0; width: 378px; top: 126px; text-align: center;
    color: #f4f1ec; font-size: 16px; letter-spacing: 0.55em;
  }
  .card--back { left: 731px; top: 728px; background: var(--paper); }
  .portrait {
    position: absolute; left: 30px; top: 20px; width: 145px; height: 165px;
    background: radial-gradient(ellipse at 50% 45%, #ddc9a2 0%, #ead9bb 45%, #fbf7f0 80%, #ffffff 100%);
  }
  .card-divider {
    position: absolute; left: 193px; top: 52px; width: 1.5px; height: 133px;
    background: var(--gold);
  }
  .card-contact {
    position: absolute; left: 213px; top: 51px;
    color: var(--gold); font-size: 11.5px; line-height: 16px;
  }
  .card-contact p { margin: 0 0 6px; }
  .card-contact .card-name { font-size: 14px; text-transform: uppercase; margin: 0; line-height: 18px; }
</style>
</head>
<body>
<main class="canvas">

  <div class="wordmark wordmark--hero">Helga Brunnmeier</div>

  <section class="letterhead">
    <div class="wordmark">Helga Brunnmeier</div>
    <div class="sender-line">Helga Brunnmeier<span class="dot"></span>Musterstraße 00<span class="dot"></span>12345 Musterstadt</div>
    <div class="address-block">
      <p>Helga Brunnmeier<br>Titel<br>Musterstraße 12<br>12345 Musterstadt</p>
      <p>T. 0123 456 789<br>F. 0123 456 789<br>info@brunnmeier-beispiel.de<br>www.helga-brunnmeier-beispiel.de</p>
    </div>
    <div class="footer-block">
      <p>Steuernr.: 123/456/78910</p>
      <p>Bankverbindung:<br>IBAN: DE12 3456 789 1253 5708 40<br>BIC:&nbsp;&nbsp;&nbsp; HELADEF1234</p>
    </div>
    <svg class="wave" width="583" height="100" viewBox="0 0 583 100" aria-hidden="true">
      <path d="M0,28 C150,-8 300,66 430,80 C500,86 560,70 583,48 L583,100 L0,100 Z" fill="var(--cream)"/>
      <path d="M0,44 C150,10 300,70 430,84 C505,88 560,74 583,58 L583,100 L0,100 Z" fill="var(--gold)"/>
    </svg>
  </section>

  <section class="card card--front">
    <div class="wordmark">Helga Brunnmeier</div>
  </section>

  <section class="card card--back">
    <div class="portrait" role="img" aria-label="Porträtfoto von Helga Brunnmeier in Goldtönen"></div>
    <div class="card-divider"></div>
    <div class="card-contact">
      <p class="card-name">Helga Brunnmeier</p>
      <p>Titel</p>
      <p>Musterstraße 12<br>12345 Musterstadt</p>
      <p>T. 0123 456 789<br>F. 0123 456 789</p>
      <p>info@brunnmeier-beispiel.de<br>www.helga-brunnmeier-beispiel.de</p>
    </div>
    <svg class="wave" width="378" height="75" viewBox="0 0 378 75" aria-hidden="true">
      <path d="M0,5 C80,-6 160,6 230,28 C290,44 340,38 378,20 L378,75 L0,75 Z" fill="var(--cream)"/>
      <path d="M0,15 C80,2 160,14 230,32 C290,48 340,42 378,24 L378,75 L0,75 Z" fill="var(--gold)"/>
    </svg>
  </section>

</main>
</body>
</html>
```